Business Card Design - Cryotherapy

We need a custom created business card for our company FrostLume Spa. We provide whole body cryotherapy and localized cryotherapy to our clients. Please be creative.
Please see our website for idea's on design.
www.frostlumespa.com
Industry/Entity Type
Business
Contact Information for Business Card
Name, Position, Phone Number, Address, Website, Email
Look and feel
Each slider illustrates characteristics of the customer's brand and the style your logo design should communicate.

```html
<!DOCTYPE html>
<html lang="en">
<head>
<meta charset="UTF-8">
<title>FrostLume Spa – Business Card</title>
<link rel="stylesheet" href="https://fonts.googleapis.com/css2?family=Open+Sans:wght@400;600&display=swap">
<style>
  :root {
    --page-bg: #e9ecec;
    --card-bg: #ffffff;
    --teal: #14968b;
    --teal-dark: #0f7a6f;
    --text: #3a3a3a;
    --mark: #3fb3a8;
  }
  * { margin: 0; padding: 0; box-sizing: border-box; }
  html, body { width: 1043px; height: 1200px; overflow: hidden; }
  body {
    background: var(--page-bg);
    font-family: "Open Sans", Arial, sans-serif;
    position: relative;
  }
  .card {
    position: absolute;
    width: 640px;
    height: 390px;
    background: var(--card-bg);
    border-radius: 18px;
    box-shadow: 0 6px 22px rgba(0,0,0,0.12);
  }
  .card--front { left: 80px; top: 150px; }
  .card--back  { left: 323px; top: 690px; }

  .brand {
    position: absolute;
    display: flex;
    align-items: center;
    gap: 12px;
    color: var(--teal-dark);
    font-weight: 600;
    white-space: nowrap;
  }
  .brand__dot {
    border-radius: 50%;
    background: var(--mark);
    flex: none;
  }
  .card--front .brand { left: 70px; top: 175px; font-size: 27px; }
  .card--front .brand__dot { width: 34px; height: 34px; }
  .card--back .brand { left: 0; right: 0; top: 160px; justify-content: center; font-size: 44px; }
  .card--back .brand__dot { width: 56px; height: 56px; }

  .contact { position: absolute; left: 350px; top: 62px; color: var(--text); }
  .contact__name { color: var(--teal); font-size: 26px; font-weight: 600; line-height: 1.2; }
  .contact__role { font-size: 16px; margin-top: 2px; }
  .contact__address { font-size: 16px; line-height: 22px; margin-top: 28px; }
  .contact__list { list-style: none; margin-top: 26px; font-size: 17px; line-height: 25px; }
  .contact__list li { display: flex; align-items: center; gap: 8px; }
  .contact__list svg { width: 13px; height: 13px; fill: var(--teal); flex: none; }
</style>
</head>
<body>
  <section class="card card--front">
    <div class="brand"><span class="brand__dot"></span>FrostLume Spa</div>
    <div class="contact">
      <div class="contact__name">Daniel Harper</div>
      <div class="contact__role">Managing Director</div>
      <div class="contact__address">1234, Address Goes Here<br>Country Name, 123456</div>
      <ul class="contact__list">
        <li><svg viewBox="0 0 16 16"><path d="M3 1l3 3-1.5 2a9 9 0 0 0 5.5 5.5L12 10l3 3-2 2C7 15 1 9 1 3z"/></svg>044-456-7890</li>
        <li><svg viewBox="0 0 16 16"><path d="M4 1h7v4H4zM1 6h14v9H1zm3 3v2h3V9zm5 0v2h3V9z"/></svg>123-456-7890</li>
        <li><svg viewBox="0 0 16 16"><path d="M4 0h8v16H4zm1.5 2v10h5V2zM8 13a1 1 0 1 0 0 .1z"/></svg>123-456-7890</li>
        <li><svg viewBox="0 0 16 16"><path d="M1 3h14v10H1zm1.5 1.5v.4L8 9l5.5-4.1v-.4z"/></svg>info@youremail.com</li>
        <li><svg viewBox="0 0 16 16"><path d="M6 10l4-4 1 1-4 4zM9 2l2-1 4 4-1 2-1.5-1.2.5-.8-2-2-.8.5zM7 14l-2 1-4-4 1-2 1.5 1.2-.5.8 2 2 .8-.5z"/></svg>www.website.com</li>
      </ul>
    </div>
  </section>

  <section class="card card--back">
    <div class="brand"><span class="brand__dot"></span>FrostLume Spa</div>
  </section>
</body>
</html>
```